Safety Training company business card design

We are after a high quality, professional business card. We are open to a single or double sided card.

The winning designer must provide the card in a format where we can easily change the name and details of the different people in our organization.

Harbor Guard's company colour is lime green.

We provide all aspects of safety advisory and training for the Building, Civil Construction, Mining, Oil and Gas, Manufacturing, Rail, Rural and Retail sectors.

Visit our website www.harborguard.com.au for training competencies we offer along with our other services including RPL's, safety audits, professional development and client support.

Target Market(s)

Those in the Building, Civil Construction, Mining, Oil and Gas, Manufacturing, Rail, Rural and Retail industries.

Industry/Entity Type

Training

Contact Information for Business Card

Harbor Guard
Safety and Training
Dennis Palworth
Director
M 0427 518 266
dennis@harborguard.com.au
www.harborguard.com.au
(2 business addresses:)
Corvin High Risk Training Centre
17 Tandem Parade, Kestrel Bay Q 4390 P 3912 5486 F 3912 5174
Brenlow Training Centre
86 Fenwick Street, Ashmere Q 4815 P 4873 2615 F 4873 2249

Colors
9bcb3c

Requirements
Must have
• Lime green must be the main colour. must include HG logo attached, and state Harbor Guard (Safety and Training in smaller/different font).

State something along the lines of:

Nice to have
• We offer remote training and we can come to you.

```html
<!DOCTYPE html>
<html lang="en">
<head>
<meta charset="utf-8">
<title>Harbor Guard – Business Card</title>
<link rel="stylesheet" href="https://fonts.googleapis.com/css2?family=Arimo:wght@400;700&display=swap">
<style>
  :root {
    --lime: #9bcb3c;
    --lime-dark: #7cb22a;
    --yellow: #f3e01c;
    --red: #c23222;
    --ink: #2e2e2e;
    --grey: #5a5a5a;
    --paper: #f7f7f5;
    --backdrop: #3a3d3c;
  }
  * { box-sizing: border-box; margin: 0; padding: 0; }
  html, body { width: 1200px; height: 900px; overflow: hidden; }
  body {
    background: var(--backdrop);
    font-family: "Arimo", Arial, sans-serif;
    display: flex; flex-direction: column; align-items: center; justify-content: center; gap: 40px;
  }
  .card {
    position: relative; width: 680px; height: 400px; overflow: hidden;
    background: var(--paper);
    box-shadow: 0 10px 30px rgba(0,0,0,.35);
  }
  .green { background: linear-gradient(160deg, var(--lime) 0%, var(--lime-dark) 100%); position: absolute; left: 0; right: 0; }
  .rule { position: absolute; left: 0; right: 0; height: 3px; background: var(--yellow); }

  .brand { position: absolute; display: flex; align-items: center; gap: 12px; }
  .brand-dot { width: 22px; height: 22px; border-radius: 50%; background: var(--red); flex: none; }
  .brand-name { font-weight: 700; color: var(--yellow); text-transform: uppercase; letter-spacing: 1px; line-height: 1; }
  .brand-tag { color: #fff; text-transform: uppercase; letter-spacing: 5px; font-size: 11px; margin-top: 6px; }

  /* back side */
  .back .green.top { top: 0; height: 250px; }
  .back .green.bottom { bottom: 0; height: 54px; }
  .back .brand { left: 0; right: 0; top: 90px; justify-content: center; }
  .back .brand-name { font-size: 42px; }
  .back .brand-dot { width: 34px; height: 34px; }
  .back .tagline {
    position: absolute; top: 262px; left: 30px; right: 30px;
    text-align: center; color: var(--ink); font-size: 15px; line-height: 1.55;
  }

  /* front side */
  .front .green.top { top: 0; height: 118px; }
  .front .green.bottom { bottom: 0; height: 16px; }
  .front .brand { left: 34px; top: 38px; }
  .front .brand-name { font-size: 30px; }
  .person { position: absolute; left: 34px; top: 146px; }
  .person::before { content: ""; position: absolute; left: -34px; top: 0; width: 7px; height: 52px; background: var(--red); }
  .person-name { font-size: 21px; font-weight: 700; color: var(--red); text-transform: uppercase; letter-spacing: .5px; }
  .person-role { font-size: 15px; color: var(--grey); font-weight: 400; }
  .person-company { font-size: 14px; color: var(--grey); text-transform: uppercase; letter-spacing: 1px; margin-top: 4px; }

  .contacts { position: absolute; left: 34px; top: 238px; font-size: 14px; color: var(--ink); letter-spacing: .5px; }
  .contact-row { display: flex; align-items: center; gap: 8px; margin-bottom: 6px; }
  .contact-row svg { width: 12px; height: 12px; flex: none; }
  .contact-pair { display: flex; gap: 28px; }
  .divider { position: absolute; left: 34px; right: 34px; top: 300px; height: 1px; background: #8a8a8a; }
  .addresses { position: absolute; left: 34px; right: 24px; top: 312px; font-size: 13.5px; color: var(--ink); line-height: 1.6; }
</style>
</head>
<body>

<section class="card back" aria-label="Card back">
  <div class="green top"></div>
  <div class="rule" style="top:250px"></div>
  <div class="brand">
    <span class="brand-dot"></span>
    <div>
      <div class="brand-name">Harbor Guard</div>
      <div class="brand-tag">Safety and Training</div>
    </div>
  </div>
  <p class="tagline">We provide all aspects of safety advisory and training for the Building,<br>Civil Construction, Mining, Oil and Gas, Manufacturing, Rail, Rural and Retail sectors</p>
  <div class="rule" style="bottom:54px"></div>
  <div class="green bottom"></div>
</section>

<section class="card front" aria-label="Card front">
  <div class="green top"></div>
  <div class="rule" style="top:118px"></div>
  <div class="brand">
    <span class="brand-dot"></span>
    <div>
      <div class="brand-name">Harbor Guard</div>
      <div class="brand-tag">Safety and Training</div>
    </div>
  </div>

  <div class="person">
    <div class="person-name">Dennis Palworth <span class="person-role">/DIRECTOR</span></div>
    <div class="person-company">Harbor Guard Safety and Training</div>
  </div>

  <div class="contacts">
    <div class="contact-row">
      <svg viewBox="0 0 12 12"><rect x="3" y="0.5" width="6" height="11" rx="1.2" fill="var(--red)"/><rect x="4.2" y="2" width="3.6" height="6" fill="#fff"/></svg>
      <span>0427 518 266</span>
    </div>
    <div class="contact-pair">
      <div class="contact-row">
        <svg viewBox="0 0 12 12"><rect x="0.7" y="2.2" width="10.6" height="7.6" fill="none" stroke="var(--red)" stroke-width="1.3"/><path d="M1 2.6 6 7l5-4.4" fill="none" stroke="var(--red)" stroke-width="1.3"/></svg>
        <span>dennis@harborguard.com.au</span>
      </div>
      <div class="contact-row">
        <svg viewBox="0 0 12 12"><circle cx="6" cy="6" r="5.2" fill="none" stroke="var(--red)" stroke-width="1.2"/><ellipse cx="6" cy="6" rx="2.2" ry="5.2" fill="none" stroke="var(--red)" stroke-width="1"/><path d="M1 6h10" stroke="var(--red)" stroke-width="1"/></svg>
        <span>www.harborguard.com.au</span>
      </div>
    </div>
  </div>

  <div class="divider"></div>
  <div class="addresses">
    <div>Corvin High Risk Training Centre 17 Tandem Parade, Kestrel Bay Q 4390 P 3912 5486 F 3912 5174</div>
    <div>Brenlow Training Centre 86 Fenwick Street, Ashmere Q 4815 P 4873 2615 F 4873 2249</div>
  </div>

  <div class="rule" style="bottom:16px"></div>
  <div class="green bottom"></div>
</section>

</body>
</html>
```